Commercial Real Estate Marketing Flyer
Property Highlights
Sir,
I(#21) had given the link, from where you can get my PDF file.
Re#3, I like the footer on the upper right/lower left as it takes less space. I am LOVING the watermark on the bottom right! Can we trying placing it behind the upper right/lower left by shrinking the white box? Then I could decide between the footer or the watermark.
Great stuff!
Can we see what it can look like in a 8.5 x 11 portrait format? I like the footer in #1.
Also on the map page, can we supersize the logo like the footer behind the map?
Good work!
what size do you prefer for the flyer? 8.5x11 landscape? Also, I have no problem in sending the file in publisher format--I've worked with publisher plenty of times.
A Great start!!! Setting the bar pretty high!
As a pdf will be fine. Good luck!
OK, I will send the flyer as a PDF - is this OK?
Henry.
I have had requests for photos and text. What I am looking for is a template that I can use repeatedly for different commercial properties. Just use stock photos and garbled text for now.I am looking for a layout that is clean and current.
The template should be made up of "boxes" where I would fill in text, tables and photos. For example page 1 consists of a photo, bullet points and contact info. Page 2 may contain a table for financial info along with more photo boxes.
Page 3 may be photo and text boxes. Page 4 would be maps along with text and table boxes. hope this helps!!
I have had alot of requests that the final be in Adobe Illustrator and not MS Publisher. To all, that is fine. We want to make it easy for everyone. We will deal with it later. So... go for it!!
Hi, send the text and logo youd like si I can draft up for you thanks...
Please give me your details.Also send me images,texts and other materials that you want to use on your flyer So that I can prepare the Flyer Design for you.
Faris Okoth
Sir I prepare the require design in Adobe Illustrator and if I get success the final file I will provide you in .pdf format. Sir if it is OK then I go a head. Because don't use MS Publisher
Thanks & Regards
Deepak Ruvari
You can see samples of the flyers uploaded in the "Read Brief" section. Good Luck!
please send link of the flyer. Thanks!
Please take a look at the samples we have uploaded along with our new Logo (thanks to IconBrio!). It must be compatible to using MS Publisher. If you want examples of flyers that we like, please private message me and I will link a few flyers.

```html
<!DOCTYPE html>
<html lang="en">
<head>
<meta charset="utf-8">
<title>Vestra Group – Property Flyer</title>
<link href="https://fonts.googleapis.com/css2?family=Open+Sans:wght@400;600;700&family=Pinyon+Script&display=swap" rel="stylesheet">
<style>
:root{
  --bg:#e9e7e3;
  --paper:#ffffff;
  --navy:#14256f;
  --blue:#2546a8;
  --sky:#6c8fd6;
  --pale:#dfe7f6;
  --ink:#333;
  --muted:#777;
  --photo-sky:#b9cbe3;
  --photo-grass:#6f8f4a;
}
*{box-sizing:border-box;margin:0;padding:0}
html,body{width:1200px;height:897px;overflow:hidden;background:var(--bg);font-family:"Open Sans",sans-serif;color:var(--ink)}
.spread{position:absolute;display:flex;box-shadow:0 4px 14px rgba(0,0,0,.25)}
.page{position:relative;background:var(--paper);overflow:hidden;flex:1}
.cover-spread{left:267px;top:58px;width:666px;height:405px}
.inside-spread{left:286px;top:470px;width:630px;height:380px}
.top-rule{position:absolute;left:0;right:0;top:0;height:12px;background:linear-gradient(90deg,var(--navy),var(--blue))}
.brand{position:absolute;display:flex;align-items:center;gap:6px;color:var(--navy);font-weight:600;letter-spacing:.5px;line-height:1.15}
.brand .dot{border-radius:50%;background:var(--blue);flex:none}
.brand small{display:block;font-size:6px;color:var(--muted);font-weight:400;letter-spacing:0;margin-top:1px}
.photo{position:absolute;background:linear-gradient(180deg,var(--photo-sky),#dde6ee 55%,var(--photo-grass) 75%,#55713a)}
.bottom-band{position:absolute;left:0;right:0;bottom:0;background:linear-gradient(90deg,var(--navy),var(--blue) 60%,var(--sky))}
.watermark{position:absolute;color:rgba(255,255,255,.35);font-weight:700;letter-spacing:2px}
.cover-front .brand{left:18px;top:16px;font-size:14px}
.cover-front .brand .dot{width:18px;height:18px}
.cover-front .photo{left:0;top:48px;width:100%;height:292px}
.cover-front .bottom-band{height:65px}
.cover-front .disclaimer{position:absolute;left:10px;top:8px;width:170px;font-size:5.5px;color:#dfe7ff;line-height:1.4}
.cover-front .watermark{right:14px;bottom:4px;font-size:34px}
.highlights{position:absolute;left:14px;top:24px;width:120px;list-style:none;font-size:6px;line-height:1.55;color:#444}
.highlights li::before{content:"•";color:var(--blue);margin-right:4px}
.map{position:absolute;left:148px;top:18px;width:170px;height:120px;background:linear-gradient(135deg,#f2ede0,#e6e0cf);border:1px solid #ccc}
.big-mark{position:absolute;left:150px;top:130px;font-size:110px;font-weight:700;color:var(--pale);letter-spacing:-4px;line-height:1}
.big-ring{position:absolute;left:150px;top:100px;width:220px;height:220px;border-radius:50%;background:radial-gradient(circle,#f3f6fc,#e4ebf7)}
.contact{position:absolute;left:150px;top:248px;font-size:7.5px;color:#555;line-height:1.5}
.contact .brand{position:static;font-size:12px;margin-bottom:10px}
.contact .brand .dot{width:20px;height:20px}
.cover-back .bottom-band{height:12px}
.pill{position:absolute;display:flex;align-items:center;gap:6px;height:16px;padding:0 12px 0 3px;border-radius:8px;background:linear-gradient(90deg,var(--navy),var(--blue));color:#fff;font-size:8px;font-weight:700}
.pill .dot{width:12px;height:12px;border-radius:50%;background:#fff}
.summary .pill{left:12px;top:14px}
.title{position:absolute;left:14px;top:32px;font-family:"Pinyon Script",cursive;font-size:24px;font-weight:400;color:#222;line-height:1.1}
.intro{position:absolute;left:14px;top:62px;width:285px;font-size:5px;line-height:1.5;color:#555}
.facts{position:absolute;left:14px;top:92px;width:130px;font-size:5px;color:#555;border-collapse:collapse}
.facts td{padding:.8px 0}
.facts td:last-child{text-align:right}
.summary .photo{left:160px;top:92px;width:140px;height:90px}
.rent-table{position:absolute;left:10px;top:198px;width:296px;border-collapse:collapse;font-size:5px;color:#444}
.rent-table th{background:var(--blue);color:#fff;font-weight:600;padding:4px 2px;text-align:center}
.rent-table td{text-align:center;padding:4px 2px;border-bottom:1px solid #e2e2e2}
.rent-table tr:last-child td{font-weight:700;border-bottom:none}
.summary .bottom-band{height:22px}
.url{position:absolute;left:12px;bottom:6px;font-size:8px;color:#fff;font-weight:600}
.market .pill{left:10px;top:14px}
.market .big-ring{left:140px;top:40px;width:220px;height:220px}
.market-row{position:absolute;left:12px;display:flex;gap:8px;width:290px}
.market-row .thumb{width:44px;height:34px;flex:none;background:linear-gradient(180deg,#a9bfdc,#cfd9e6 50%,#8a9a6c)}
.market-row p{font-size:4.6px;line-height:1.5;color:#555;position:relative}
.market .bottom-band{height:22px}
.market .watermark{right:12px;bottom:0;font-size:20px}
</style>
</head>
<body>

<section class="spread cover-spread">
  <article class="page cover-front">
    <div class="top-rule"></div>
    <div class="brand"><span class="dot"></span><div>VESTRA GROUP<small>Commercial Real Estate Services</small></div></div>
    <div class="photo" role="img" aria-label="Photo of the apartment property with entrance sign and lawn"></div>
    <div class="bottom-band">
      <p class="disclaimer">Information deemed reliable but not guaranteed. Subject to change without notice.</p>
      <span class="watermark">VG</span>
    </div>
  </article>
  <article class="page cover-back">
    <div class="top-rule"></div>
    <div class="big-ring"></div>
    <ul class="highlights">
      <li>Neighborhood retail center</li>
      <li>Built in 1998</li>
      <li>Fully leased, stable tenants</li>
      <li>Close to major freeway access</li>
      <li>Ample on-site parking</li>
      <li>Strong local demographics</li>
      <li>Recent roof upgrades</li>
      <li>High traffic corner lot</li>
      <li>Flexible suite sizes</li>
      <li>Below market rents</li>
      <li>Value-add opportunity</li>
    </ul>
    <div class="map" role="img" aria-label="Street map showing property location"></div>
    <div class="big-mark">VG</div>
    <div class="contact">
      <div class="brand"><span class="dot"></span>VESTRA GROUP</div>
      <div>VESTRA GROUP</div>
      <div>418 W Harlow Ave, Suite 210, Marlow, CA 90000</div>
      <div>Phone 555-014-2200 Fax 555-014-2288</div>
    </div>
    <div class="bottom-band"></div>
  </article>
</section>

<section class="spread inside-spread">
  <article class="page summary">
    <div class="pill"><span class="dot"></span>Investment Summary</div>
    <h1 class="title">Linden Court</h1>
    <p class="intro">A well kept garden apartment community set among mature trees, offering steady occupancy and a solid income history in an established neighborhood close to schools, shopping and transit.</p>
    <table class="facts">
      <tr><td>Price</td><td>$2,450,000</td></tr>
      <tr><td>Units</td><td>48</td></tr>
      <tr><td>Price/Unit</td><td>$51,040</td></tr>
      <tr><td>Cap Rate</td><td>6.8%</td></tr>
      <tr><td>GRM</td><td>8.9</td></tr>
      <tr><td>Year Built</td><td>1978</td></tr>
      <tr><td>Lot Size</td><td>2.1 Acres</td></tr>
      <tr><td>Building</td><td>38,400 SF</td></tr>
      <tr><td>Parking</td><td>72 Spaces</td></tr>
      <tr><td>Occupancy</td><td>96%</td></tr>
    </table>
    <div class="photo" role="img" aria-label="Photo of the property entrance sign"></div>
    <table class="rent-table">
      <tr><th>Unit Type</th><th>Units</th><th>Sq Ft</th><th>Rent</th><th>Rent/SF</th><th>Annual Income</th><th>Market Rent</th><th>Rent/SF</th></tr>
      <tr><td>1 Bed 1 Bath</td><td>12</td><td>650</td><td>$625</td><td>$0.96</td><td>$90,000</td><td>$650</td><td>$1.00</td></tr>
      <tr><td>2 Bed 1 Bath</td><td>16</td><td>850</td><td>$725</td><td>$0.85</td><td>$139,200</td><td>$750</td><td>$0.88</td></tr>
      <tr><td>2 Bed 2 Bath</td><td>12</td><td>950</td><td>$795</td><td>$0.84</td><td>$114,480</td><td>$825</td><td>$0.87</td></tr>
      <tr><td>3 Bed 2 Bath</td><td>8</td><td>1,150</td><td>$925</td><td>$0.80</td><td>$88,800</td><td>$950</td><td>$0.83</td></tr>
      <tr><td>Total</td><td>48</td><td>40,600</td><td></td><td></td><td>$432,480</td><td></td><td></td></tr>
    </table>
    <div class="bottom-band"><span class="url">www.vestragroup.com</span></div>
  </article>
  <article class="page market">
    <div class="big-ring"></div>
    <div class="pill"><span class="dot"></span>Market Overview</div>
    <div class="market-row" style="top:40px"><div class="thumb" role="img" aria-label="Photo of nearby townhomes"></div><p>The surrounding area has seen steady growth, with new housing and retail drawing young families and professionals who value quiet streets and quick commutes.</p></div>
    <div class="market-row" style="top:84px"><div class="thumb" role="img" aria-label="Photo of comparable apartment building"></div><p>Comparable properties nearby report high occupancy and rising rents, supported by limited new supply and strong demand from local employers.</p></div>
    <div class="market-row" style="top:128px"><div class="thumb" role="img" aria-label="Photo of local shopping center"></div><p>Residents enjoy easy access to grocery stores, dining, parks and medical offices, all within a short drive of the property entrance.</p></div>
    <div class="market-row" style="top:172px"><div class="thumb" role="img" aria-label="Photo of downtown skyline"></div><p>The regional economy is anchored by education, healthcare and agriculture, providing a stable base of jobs and long term tenant demand.</p></div>
    <div class="market-row" style="top:216px"><div class="thumb" role="img" aria-label="Photo of residential street"></div><p>Planned road improvements and new schools are expected to further boost values and attract households to the neighborhood.</p></div>
    <div class="market-row" style="top:260px"><div class="thumb" role="img" aria-label="Photo of community park"></div><p>Overall, the market offers investors a balanced mix of current income and future appreciation potential.</p></div>
    <div class="bottom-band"><span class="watermark">VG</span></div>
  </article>
</section>

</body>
</html>
```